BOLD & MINIMALIST DESIGN NEEDED

We want a very bold but minimalistic business card design that is impactful and utilizes both sides of the business card. Our current logo is included for your use.

We want bold fonts and good use of negative space. We don't want the logo to overpower the design.

Target Market(s)

Professionals who are building new commercial buildings.

Industry/Entity Type

Construction

Contact Information for Business Card

Name, Title, email, office phone, cell phone, website

Font styles to use
Serif
Sans Serif

Requirements
Must have
• Bold design!

```html
<!DOCTYPE html>
<html lang="en">
<head>
<meta charset="utf-8">
<title>Ridgeline Design + Build — Business Card</title>
<link rel="stylesheet" href="https://fonts.googleapis.com/css2?family=Montserrat:wght@500;600;700;800&display=swap">
<style>
  :root {
    --page-bg: #ececea;
    --card-dark: #1b1b1b;
    --card-light: #ffffff;
    --ink: #141414;
    --accent: #7dc242;
    --rule: #222222;
  }
  * { box-sizing: border-box; margin: 0; padding: 0; }
  html, body { width: 1200px; height: 1200px; overflow: hidden; }
  body {
    background: var(--page-bg);
    font-family: "Montserrat", Arial, sans-serif;
    position: relative;
  }
  .card {
    position: absolute;
    left: 216px;
    width: 768px;
    height: 426px;
    border-radius: 28px;
    box-shadow: 0 6px 18px rgba(0,0,0,0.18);
    overflow: hidden;
  }
  .card--front { top: 158px; background: var(--card-dark); }
  .card--back { top: 617px; background: var(--card-light); }

  .brand {
    position: absolute;
    display: flex;
    align-items: center;
    gap: 14px;
  }
  .brand__mark { width: 22px; height: 22px; background: var(--accent); flex: none; }
  .brand__name {
    font-weight: 800;
    text-transform: uppercase;
    line-height: 1.05;
    letter-spacing: 0.02em;
  }
  .card--front .brand {
    left: 0; right: 0; top: 0; bottom: 0;
    justify-content: center;
  }
  .card--front .brand__mark { width: 30px; height: 30px; }
  .card--front .brand__name { color: #ffffff; font-size: 50px; text-align: center; }
  .card--back .brand { left: 50px; top: 150px; width: 320px; }
  .card--back .brand__name { color: var(--ink); font-size: 30px; }

  .divider {
    position: absolute;
    left: 407px; top: 96px;
    width: 2px; height: 233px;
    background: var(--rule);
  }
  .contact { position: absolute; left: 447px; top: 96px; color: var(--ink); }
  .contact__name { font-size: 31px; font-weight: 700; line-height: 1.2; }
  .contact__title { font-size: 20px; font-weight: 600; margin-top: 6px; }
  .contact__list { list-style: none; margin-top: 30px; }
  .contact__item {
    display: flex; align-items: center; gap: 12px;
    font-size: 21px; font-weight: 600; height: 36px;
  }
  .contact__icon { width: 20px; height: 20px; flex: none; }
</style>
</head>
<body>
  <section class="card card--front">
    <div class="brand">
      <span class="brand__mark"></span>
      <span class="brand__name">Ridgeline<br>Design + Build</span>
    </div>
  </section>

  <section class="card card--back">
    <div class="brand">
      <span class="brand__mark"></span>
      <span class="brand__name">Ridgeline<br>Design + Build</span>
    </div>
    <div class="divider"></div>
    <div class="contact">
      <p class="contact__name">Marcus Elwood</p>
      <p class="contact__title">Founder &amp; CEO</p>
      <ul class="contact__list">
        <li class="contact__item">
          <svg class="contact__icon" viewBox="0 0 20 20"><path fill="var(--accent)" d="M2 7c0-3 4-4 8-4s8 1 8 4v2h-4V7H6v2H2z M5 10h10l2 7H3z"/><circle cx="10" cy="13.5" r="2" fill="#fff"/></svg>
          <span>555-014-2200</span>
        </li>
        <li class="contact__item">
          <svg class="contact__icon" viewBox="0 0 20 20"><rect x="5" y="1.5" width="10" height="17" rx="2" fill="none" stroke="var(--accent)" stroke-width="1.8"/><circle cx="10" cy="15.5" r="1" fill="var(--accent)"/></svg>
          <span>555-014-2201</span>
        </li>
        <li class="contact__item">
          <svg class="contact__icon" viewBox="0 0 20 20"><rect x="1.5" y="4.5" width="17" height="11" fill="var(--accent)"/><path d="M1.5 4.5l8.5 6.5 8.5-6.5" fill="none" stroke="#fff" stroke-width="1.4"/></svg>
          <span>info@ridgeline-db.com</span>
        </li>
        <li class="contact__item">
          <svg class="contact__icon" viewBox="0 0 20 20"><circle cx="10" cy="10" r="8.5" fill="var(--accent)"/><ellipse cx="10" cy="10" rx="3.5" ry="8.5" fill="none" stroke="#fff" stroke-width="1.2"/><path d="M1.5 10h17" stroke="#fff" stroke-width="1.2"/></svg>
          <span>www.ridgeline-db.com</span>
        </li>
      </ul>
    </div>
  </section>
</body>
</html>
```